DOG DAYCARE BILLBOARD

Design a bold exciting billboard that can be read easily from a distance! Our goal is brand awareness and showcasing the services we offer (Boarding, Grooming, Daycare, and Training.
we would like to see examples with the phrase "your best friend's best day". Our name Bright Meadow Canine Activity Center (or just Bright Meadow might work better and could be bigger) and the services we provide.
(there are two examples of what we like included in the pictures)
you can find more information o our website at pawplayhouse@mailbox-example.com.

```html
<!DOCTYPE html>
<html lang="en">
<head>
<meta charset="utf-8">
<title>Bright Meadow Billboard</title>
<link rel="stylesheet" href="https://fonts.googleapis.com/css2?family=Jost:wght@400;500;700;800;900&display=swap">
<style>
  :root {
    --brand-green: #5aff0a;
    --ink: #1f1c1d;
    --paper: #ffffff;
    --photo-dark: #3f6b2a;
    --photo-mid: #8fb35a;
    --photo-tan: #c99a5e;
  }
  * { margin: 0; padding: 0; box-sizing: border-box; }
  html, body {
    width: 1200px; height: 1200px; overflow: hidden;
    background: var(--paper);
    font-family: "Jost", "Futura", sans-serif;
    color: var(--ink);
  }
  .billboard {
    position: absolute; left: 45px; top: 343px;
    width: 1110px; height: 514px;
    border: 1px solid var(--ink);
    background: var(--paper);
  }
  .billboard__top {
    position: absolute; left: 0; top: 0; width: 100%; height: 379px;
    background: var(--brand-green);
  }
  .headline {
    position: absolute; left: 0; top: 30px; width: 100%;
    text-align: center; font-weight: 800; font-size: 67px;
    line-height: 1; letter-spacing: 0.5px; white-space: nowrap;
  }
  .brand {
    position: absolute; left: 70px; top: 200px;
    display: flex; align-items: center; gap: 14px;
  }
  .brand__dot {
    width: 30px; height: 30px; border-radius: 50%;
    background: var(--ink);
  }
  .brand__name {
    font-weight: 800; font-size: 48px; line-height: 1; white-space: nowrap;
  }
  .services {
    position: absolute; left: 558px; top: 126px;
    width: 468px; height: 224px;
    background: var(--paper);
    border: 3px solid var(--ink); border-radius: 26px;
    overflow: hidden;
  }
  .services__photo {
    position: absolute; left: 0; top: 0; width: 178px; height: 100%;
    background: linear-gradient(160deg, var(--photo-dark) 0%, var(--photo-mid) 40%, var(--photo-tan) 70%, var(--photo-dark) 100%);
  }
  .services__list {
    position: absolute; left: 200px; top: 14px;
    list-style: none;
  }
  .services__item {
    display: flex; align-items: center; gap: 14px;
    height: 51px; font-weight: 800; font-size: 34px; line-height: 1;
  }
  .services__item::before {
    content: ""; width: 22px; height: 22px; border-radius: 50%;
    background: var(--brand-green); flex: none; margin-top: -10px;
  }
  .contact-row {
    position: absolute; left: 46px; top: 390px; right: 40px;
    display: flex; align-items: center; gap: 22px;
    white-space: nowrap;
  }
  .contact-call {
    font-size: 37px; font-weight: 400; line-height: 1;
  }
  .contact-call strong { font-weight: 700; font-size: 51px; letter-spacing: -0.5px; }
  .contact-online {
    font-size: 24px; line-height: 1.15;
  }
  .contact-online strong { font-weight: 800; }
  .address {
    position: absolute; left: 0; top: 457px; width: 100%;
    text-align: center; font-size: 21px; font-weight: 500;
  }
</style>
</head>
<body>
  <section class="billboard">
    <div class="billboard__top">
      <h1 class="headline">YOUR BEST FRIEND’S BEST DAY</h1>
      <div class="brand">
        <span class="brand__dot"></span>
        <span class="brand__name">Bright Meadow</span>
      </div>
      <div class="services">
        <div class="services__photo" role="img" aria-label="Photo of a happy tan dog among tall green grass"></div>
        <ul class="services__list">
          <li class="services__item">BOARDING</li>
          <li class="services__item">GROOMING</li>
          <li class="services__item">DAYCARE</li>
          <li class="services__item">TRAINING</li>
        </ul>
      </div>
    </div>
    <div class="contact-row">
      <p class="contact-call">Call: <strong>(555) 318-2046</strong></p>
      <p class="contact-online">Email: <strong>pawplayhouse@mailbox-example.com</strong><br>web: <strong>www.brightmeadowcanine.example</strong></p>
    </div>
    <p class="address">Bright Meadow Canine Activity Center, 418 W Orchard Ave. Millbrook, IA 50999</p>
  </section>
</body>
</html>
```